Packaging Design job - Product : Supplement for Travel Sickness

We need a packaging design for a travel sickness supplement called "VOLUMAR"

VOLUMAR It is a dietary supplement based on ginger which has properties fighting against motion sickness.

Ginger is a root used for many years for its beneficial effects on health. In addition to its stimulating and toning properties which help to resist fatigue, ginger is used as an adjuvant in case of nausea, vomiting and motion sickness. Ideal for pregnant women to combat certain disadvantages of pregnancy.

This product will be in blister form of 30 capsules. We need for this a packaging design for the box.Dimensions: 100 * 20 * 200 mm

We would like to see clean, modern and fresh designs.This should give the impression of professional products of pharmaceutical quality. You will also find attached the logo of our company.Ps : You can change the color of the logo

Mention to put on the box :

• Produit en France: Laboratoire KRANIVO, 24 Rue des Lavandières 37410 BRÉCHAL
• Distribué au Maroc: LUMORAXIN 14 rue Oumaima Tazrouti 30050 FEZ MAROC
• Complément alimentaire, ce n'est pas un médicament
• Voie orale
• Tenir hors de portée des enfants
• Respectez la dose recommandée
• Ce produit ne remplace pas une alimentation variée

Mode d'utilisation (How to use) :

2 à 3 gélules 30 min avant de prendre le véhicule de transport
1 gélule par jour en cas de cure

Font styles to use
Serif
Sans Serif
Script

Requirements
Should not have
• Sales and other "must buy" "guaranteed" etc

```html
<!DOCTYPE html>
<html lang="fr">
<head>
<meta charset="utf-8">
<title>VOLUMAR – dieline boîte 30 gélules</title>
<link rel="stylesheet" href="https://fonts.googleapis.com/css2?family=Roboto:ital,wght@0,400;0,700;0,900;1,400;1,700;1,900&family=Lato:ital,wght@0,300;0,400;1,400;1,700&display=swap">
<style>
  :root {
    --paper: #ffffff;
    --page: #ffffff;
    --cut: #9a9a9a;
    --title-grey: #555759;
    --ink: #2e2e2e;
    --navy: #22314b;
    --steel: #6e84a0;
    --mist: #c9dbe6;
    --ice: #e9f1f6;
  }
  * { box-sizing: border-box; margin: 0; padding: 0; }
  html, body { width: 1159px; height: 1200px; overflow: hidden; background: var(--page); }
  .canvas { position: relative; width: 1159px; height: 1200px; }
  .dieline { position: absolute; inset: 0; }

  .wave-field { position: absolute; left: 135px; width: 876px; }
  .wave-field--back {
    top: 157px; height: 443px;
    background: linear-gradient(168deg, var(--paper) 0%, var(--ice) 25%, var(--paper) 40%, var(--mist) 58%, var(--steel) 68%, var(--navy) 74%, var(--mist) 82%, var(--ice) 90%, var(--paper) 100%);
  }
  .wave-field--front {
    top: 686px; height: 440px;
    background: linear-gradient(172deg, var(--mist) 0%, var(--ice) 10%, var(--steel) 22%, var(--navy) 27%, var(--mist) 34%, var(--paper) 48%, var(--ice) 68%, var(--paper) 78%, var(--mist) 100%);
  }

  /* Back panel, printed upside down */
  .back-panel {
    position: absolute; left: 135px; top: 75px; width: 876px; height: 525px;
    transform: rotate(180deg);
    font-family: "Roboto", Arial, sans-serif; color: var(--ink);
  }
  .back-panel .brand { position: absolute; left: 45px; top: 440px; }
  .brand-name {
    font-family: "Roboto", Arial, sans-serif; font-weight: 900; font-style: italic;
    color: var(--title-grey); letter-spacing: 1px; line-height: 1;
  }
  .brand-tagline { font-family: "Lato", Arial, sans-serif; font-style: italic; color: var(--ink); }
  .back-panel .brand-name { font-size: 56px; }
  .back-panel .brand-tagline { font-size: 11px; margin-top: 14px; }

  .notices { position: absolute; left: 45px; top: 240px; width: 670px; font-size: 16px; line-height: 19px; }
  .notices ul { list-style: none; padding-left: 2px; }
  .notices li::before { content: "•"; margin-right: 9px; }
  .notices .rule { border-top: 2px solid var(--ink); margin: 8px 0 6px; }
  .notices strong { font-weight: 700; }

  .usage-badge { position: absolute; left: 33px; top: 0; width: 224px; height: 238px; }
  .usage-badge svg { position: absolute; inset: 0; }
  .usage-text { position: relative; padding: 44px 14px 0; text-align: center; font-size: 15px; line-height: 20px; }
  .usage-text h3 { font-size: 15px; font-weight: 700; margin-bottom: 18px; }

  /* Side strip */
  .side-strip { position: absolute; left: 135px; top: 600px; width: 876px; height: 86px; }
  .side-strip .brand { position: absolute; left: 82px; top: 10px; }
  .side-strip .brand-name { font-size: 52px; }
  .side-strip .brand-tagline { font-size: 11px; margin-top: 6px; }
  .side-copy {
    position: absolute; left: 462px; top: 15px; width: 410px;
    font-family: "Roboto", Arial, sans-serif; font-weight: 700; font-size: 8.6px; line-height: 12px; color: var(--ink);
  }

  /* Front */
  .route-badge { position: absolute; left: 211px; top: 686px; width: 157px; height: 135px; }
  .route-badge svg { position: absolute; inset: 0; }
  .route-label {
    position: relative; padding-top: 52px; text-align: center;
    font-family: "Roboto", Arial, sans-serif; font-weight: 900; font-style: italic; font-size: 27px; line-height: 28px; color: var(--title-grey);
  }
  .front-brand { position: absolute; left: 398px; top: 970px; width: 470px; text-align: center; }
  .front-brand .brand-name { font-size: 84px; }
  .front-brand .brand-tagline { font-size: 14px; margin-top: 6px; }
  .count { position: absolute; left: 905px; top: 1015px; width: 90px; text-align: center; font-family: "Lato", Arial, sans-serif; color: var(--ink); }
  .count-number { font-size: 48px; font-weight: 300; line-height: 1; }
  .count-unit { font-size: 17px; font-style: italic; }
</style>
</head>
<body>
<div class="canvas">

  <svg class="dieline" width="1159" height="1200" viewBox="0 0 1159 1200" aria-hidden="true">
    <g fill="var(--paper)" stroke="var(--cut)" stroke-width="1.2">
      <!-- left flaps -->
      <path d="M135,75 L64,92 L54,146 L135,157 Z"/>
      <path d="M135,160 H104 Q54,160 54,210 V552 Q54,600 104,600 H135"/>
      <path d="M135,600 L64,612 L54,676 L135,686 Z"/>
      <path d="M135,688 H104 Q54,688 54,738 V1076 Q54,1126 104,1126 H135"/>
      <!-- right flaps -->
      <path d="M1011,75 L1082,92 L1092,146 L1011,157 Z"/>
      <path d="M1011,160 H1042 Q1092,160 1092,210 V552 Q1092,600 1042,600 H1011"/>
      <path d="M1011,600 L1082,612 L1092,676 L1011,686 Z"/>
      <path d="M1011,688 H1042 Q1092,688 1092,738 V1076 Q1092,1126 1042,1126 H1011"/>
      <!-- body -->
      <rect x="135" y="75" width="876" height="1051"/>
    </g>
  </svg>

  <div class="wave-field wave-field--back" role="img" aria-label="Vagues abstraites bleu acier et blanc"></div>
  <div class="wave-field wave-field--front" role="img" aria-label="Vagues abstraites bleu acier et blanc"></div>

  <svg class="dieline" width="1159" height="1200" viewBox="0 0 1159 1200" aria-hidden="true">
    <g fill="none" stroke="var(--cut)" stroke-width="1">
      <line x1="135" y1="600" x2="1011" y2="600"/>
      <line x1="135" y1="686" x2="1011" y2="686"/>
      <rect x="135" y="75" width="876" height="1051"/>
    </g>
  </svg>

  <section class="back-panel">
    <div class="usage-badge">
      <svg width="224" height="238" viewBox="0 0 224 238" aria-hidden="true">
        <polygon points="0,0 224,0 224,212 112,238 0,212" fill="var(--paper)"/>
      </svg>
      <div class="usage-text">
        <h3>Mode d'utilisation</h3>
        <p>2 à 3 gélules 30 min<br>avant de prendre le<br>véhicule de transport<br>1 gélule par jour<br>en cas de cure</p>
      </div>
    </div>

    <div class="notices">
      <ul>
        <li>Tenir hors de portée des enfants</li>
        <li>Respectez la dose recommandée</li>
        <li>Ce produit ne remplace pas une alimentation variée</li>
      </ul>
      <div class="rule"></div>
      <p><strong>Produit en France:</strong><br>Laboratoire KRANIVO, 24 Rue des Lavandières 37410 BRÉCHAL</p>
      <div class="rule"></div>
      <p><strong>Distribué au Maroc:</strong><br>LUMORAXIN 14 rue Oumaima Tazrouti 30050 FEZ MAROC</p>
    </div>

    <div class="brand">
      <h2 class="brand-name">VOLUMAR</h2>
      <p class="brand-tagline">Complément alimentaire, &nbsp;ce n'est pas un médicament</p>
    </div>
  </section>

  <section class="side-strip">
    <div class="brand">
      <h2 class="brand-name">VOLUMAR</h2>
      <p class="brand-tagline">Complément alimentaire, &nbsp;ce n'est pas un médicament</p>
    </div>
    <p class="side-copy">Lorem ipsum dolor sit amet, consectetuer adipiscing elit, sed diam nonummy nibh euismod tincidunt ut laoreet dolore magna aliquam erat volutpat. Ut wisi enim ad minim veniam, quis nostrud exerci tation ullamcorper suscipit lobortis nisl ut aliquip ex ea commodo consequat. Duis autem vel eum iriure dolor in hendrerit in vulputate</p>
  </section>

  <div class="route-badge">
    <svg width="157" height="135" viewBox="0 0 157 135" aria-hidden="true">
      <polygon points="0,0 157,0 157,106 78.5,135 0,106" fill="var(--paper)"/>
    </svg>
    <p class="route-label">VOIE<br>ORALE</p>
  </div>

  <div class="front-brand">
    <h1 class="brand-name">VOLUMAR</h1>
    <p class="brand-tagline">Complément alimentaire, &nbsp;ce n'est pas un médicament</p>
  </div>

  <div class="count">
    <div class="count-number">30</div>
    <div class="count-unit">Capsules</div>
  </div>

</div>
</body>
</html>
```